Commercial Business Card - stand out, clean, simple, unique.

commercial real estate group located in Texas. Called 4 Ridges Real Estate. We want a unique yet clean and professional card. On one side I would like the 4R to be by itself or to look as unique or tasteful as possible. We have the logo in white, black, and color in case a black background or something similar looks best on one side. We need a space for our name, email, cell. website. And possibly room for a phrase or city.

Contact Information for Business Card

Name, Title, Email, Phone Number, website

```html
<!DOCTYPE html>
<html lang="en">
<head>
<meta charset="utf-8">
<title>4 Ridges Real Estate — Business Card</title>
<link rel="stylesheet" href="https://fonts.googleapis.com/css2?family=Cinzel:wght@500&family=Montserrat:wght@400;500&display=swap">
<style>
  :root {
    --stage: #2e2e30;
    --navy-deep: #17286f;
    --navy: #1f3a93;
    --navy-bright: #2c4bb3;
    --ink: #1d3a8a;
    --paper: #ffffff;
    --paper-shade: #eef0f4;
    --accent: #e0662f;
    --rule: #2a4a9e;
  }
  * { margin: 0; padding: 0; box-sizing: border-box; }
  html, body { width: 1200px; height: 900px; overflow: hidden; }
  body { background: var(--stage); position: relative; font-family: "Montserrat", Arial, sans-serif; }

  .card {
    position: absolute;
    left: 250px;
    width: 700px;
    height: 400px;
    overflow: hidden;
  }
  .card--front {
    top: 40px;
    background: linear-gradient(135deg, var(--navy-deep) 0%, var(--navy) 55%, var(--navy-bright) 100%);
  }
  .card--back {
    top: 470px;
    background: linear-gradient(100deg, var(--paper) 0%, var(--paper) 55%, var(--paper-shade) 100%);
  }

  .brand-name {
    position: absolute;
    font-family: "Cinzel", Georgia, serif;
    font-weight: 500;
    letter-spacing: 1px;
    white-space: nowrap;
    font-size: 30px;
    line-height: 36px;
  }
  .card--front .brand-name { left: 70px; top: 170px; color: var(--paper); }
  .card--back .brand-name { left: 60px; top: 72px; color: var(--ink); }

  .back-band {
    position: absolute; left: 0; right: 0; bottom: 0; height: 14px;
    background: var(--navy);
  }
  .rule { position: absolute; height: 1.5px; background: var(--rule); }
  .rule--top { left: 330px; width: 320px; top: 146px; }
  .rule--name { left: 250px; width: 200px; top: 234px; }

  .person-name {
    position: absolute; left: 60px; top: 220px;
    font-size: 19px; line-height: 24px; font-weight: 500; letter-spacing: 0.5px;
    color: var(--ink); white-space: nowrap;
  }
  .person-title {
    position: absolute; left: 60px; top: 247px;
    font-size: 11.5px; line-height: 14px; font-weight: 500; letter-spacing: 1.4px;
    color: var(--ink); white-space: nowrap;
  }
  .address {
    position: absolute; left: 470px; top: 160px;
    font-size: 15px; line-height: 21px; font-weight: 400; font-style: normal;
    color: var(--ink); white-space: nowrap;
  }
  .contact-list { position: absolute; left: 60px; top: 274px; list-style: none; }
  .contact-item {
    display: flex; align-items: center; gap: 10px;
    height: 27px;
    font-size: 15px; color: var(--ink); white-space: nowrap;
  }
  .contact-icon { width: 16px; height: 16px; flex: none; }
</style>
</head>
<body>

  <section class="card card--front" aria-label="Card front">
    <div class="brand-name">4 Ridges Real Estate</div>
  </section>

  <section class="card card--back" aria-label="Card back">
    <div class="brand-name">4 Ridges Real Estate</div>
    <div class="rule rule--top"></div>

    <address class="address">
      48 Cedar Ridge Road<br>Austin, Texas<br>78701
    </address>

    <div class="person-name">DANIEL HARLOW</div>
    <div class="person-title">MANAGING DIRECTOR</div>
    <div class="rule rule--name"></div>

    <ul class="contact-list">
      <li class="contact-item">
        <svg class="contact-icon" viewBox="0 0 16 16" aria-hidden="true">
          <rect width="16" height="16" rx="3" fill="var(--accent)"/>
          <path d="M5 4h2l1 2.5-1.2.8a5 5 0 0 0 1.9 1.9l.8-1.2L12 9v2a1 1 0 0 1-1 1A7 7 0 0 1 4 5a1 1 0 0 1 1-1z" fill="#fff"/>
        </svg>
        512 830 47 16
      </li>
      <li class="contact-item">
        <svg class="contact-icon" viewBox="0 0 16 16" aria-hidden="true">
          <rect width="16" height="16" rx="3" fill="var(--accent)"/>
          <rect x="3.5" y="5" width="9" height="6.5" rx="0.8" fill="none" stroke="#fff" stroke-width="1.2"/>
          <path d="M3.8 5.4 8 8.6l4.2-3.2" fill="none" stroke="#fff" stroke-width="1.2"/>
        </svg>
        d.harlow@4ridgesrealestate.com
      </li>
      <li class="contact-item">
        <svg class="contact-icon" viewBox="0 0 16 16" aria-hidden="true">
          <rect width="16" height="16" rx="3" fill="var(--accent)"/>
          <circle cx="8" cy="8" r="4.5" fill="none" stroke="#fff" stroke-width="1.1"/>
          <ellipse cx="8" cy="8" rx="2" ry="4.5" fill="none" stroke="#fff" stroke-width="1"/>
          <path d="M3.5 8h9" stroke="#fff" stroke-width="1"/>
        </svg>
        www.4ridgesrealestate.com
      </li>
    </ul>

    <div class="back-band"></div>
  </section>

</body>
</html>
```